Business Card Design Project

Looking for a business card that our customers will remember. We are a high end Travel Agency.
Need a re-memorable classy business card.
Both sides full color.
Must have the following details.
Voyage Harbor Logo (see attached)
4B Wattle Lane
Penhurst Sydney NSW 2241
Phone: 02 9471 3652
Fax: 02 9563 4417
sales@voyageharbor-example.com.au
Consultant Name
Anything else you think we need

```html
<!DOCTYPE html>
<html lang="en">
<head>
<meta charset="utf-8">
<title>Voyage Harbor – Business Card</title>
<link rel="stylesheet" href="https://fonts.googleapis.com/css2?family=Mulish:wght@400;700&display=swap">
<style>
  :root {
    --page: #2a2c2e;
    --card-top: #2d3d50;
    --card-bottom: #1e2a39;
    --mist: #b7cad5;
    --mist-deep: #8ea6b6;
    --band: #0c2470;
    --band-light: #1a3590;
    --gold: #e3aa1f;
    --label: #d0612c;
    --ink: #c9d0d6;
    --ink-strong: #eef1f3;
    --logo: #dcd8bd;
    --rule: rgba(200, 210, 220, .45);
  }
  * { margin: 0; padding: 0; box-sizing: border-box; }
  html, body { width: 1200px; height: 741px; overflow: hidden; }
  body {
    background: var(--page);
    font-family: "Mulish", sans-serif;
    position: relative;
  }
  .card {
    position: absolute;
    top: 216px;
    width: 540px;
    height: 309px;
    overflow: hidden;
    border-radius: 3px;
    box-shadow: 0 10px 30px rgba(0,0,0,.45);
  }
  .card--back { left: 40px; }
  .card--front { left: 620px; }
  .card-art { position: absolute; inset: 0; width: 100%; height: 100%; }

  .logo {
    position: absolute;
    display: flex;
    align-items: center;
    gap: 8px;
    color: var(--logo);
    font-weight: 400;
    font-size: 22px;
    letter-spacing: .5px;
    white-space: nowrap;
  }
  .logo-dot {
    width: 10px; height: 10px;
    border-radius: 50%;
    background: var(--logo);
  }
  .card--front .logo { left: 258px; top: 58px; }
  .card--back .logo { left: 250px; top: 138px; }

  .name-ghost {
    position: absolute;
    left: 38px; top: 92px;
    font-size: 52px;
    font-weight: 400;
    color: rgba(180, 200, 215, .10);
    letter-spacing: 2px;
    white-space: nowrap;
  }

  .divider {
    position: absolute;
    left: 296px; top: 118px;
    width: 1px; height: 96px;
    background: var(--rule);
  }
  .address {
    position: absolute;
    left: 316px; top: 118px;
    font-size: 11px;
    line-height: 14px;
    color: var(--ink);
  }
  .label { color: var(--label); }

  .consultant {
    position: absolute;
    left: 36px; top: 158px;
    font-size: 23px;
    font-weight: 700;
    color: var(--ink-strong);
  }
  .contacts {
    position: absolute;
    left: 36px; top: 196px;
    font-size: 11px;
    line-height: 14px;
    color: var(--ink);
  }
  .contacts .label { display: inline-block; width: 48px; }
</style>
</head>
<body>

<section class="card card--back" aria-label="Card back">
  <svg class="card-art" viewBox="0 0 540 309" aria-hidden="true">
    <defs>
      <linearGradient id="bgBack" x1="0" y1="0" x2="0" y2="1">
        <stop offset="0" stop-color="var(--card-top)"/>
        <stop offset="1" stop-color="var(--card-bottom)"/>
      </linearGradient>
    </defs>
    <rect width="540" height="309" fill="url(#bgBack)"/>
    <path d="M0 0 H480 C380 34 200 74 0 172 Z" fill="var(--mist-deep)" opacity=".45"/>
    <path d="M0 0 H320 C210 22 95 62 0 112 Z" fill="var(--mist)" opacity=".55"/>
    <path d="M0 309 V282 C180 258 400 216 540 166 V309 Z" fill="var(--band)"/>
    <path d="M0 309 V296 C200 280 400 250 540 206 V309 Z" fill="var(--band-light)" opacity=".5"/>
    <path d="M0 279 C180 255 400 213 540 163" fill="none" stroke="var(--gold)" stroke-width="3"/>
  </svg>
  <div class="name-ghost">Voyage Harbor</div>
  <div class="logo"><span class="logo-dot"></span>Voyage Harbor</div>
</section>

<section class="card card--front" aria-label="Card front">
  <svg class="card-art" viewBox="0 0 540 309" aria-hidden="true">
    <defs>
      <linearGradient id="bgFront" x1="0" y1="0" x2="0" y2="1">
        <stop offset="0" stop-color="var(--card-top)"/>
        <stop offset="1" stop-color="var(--card-bottom)"/>
      </linearGradient>
    </defs>
    <rect width="540" height="309" fill="url(#bgFront)"/>
    <path d="M0 0 H540 V10 C400 30 200 80 0 168 Z" fill="var(--mist-deep)" opacity=".45"/>
    <path d="M0 0 H380 C250 20 110 58 0 110 Z" fill="var(--mist)" opacity=".55"/>
    <path d="M0 309 V284 C180 262 400 222 540 172 V309 Z" fill="var(--band)"/>
    <path d="M0 309 V298 C200 284 400 256 540 212 V309 Z" fill="var(--band-light)" opacity=".5"/>
    <path d="M0 281 C180 259 400 219 540 169" fill="none" stroke="var(--gold)" stroke-width="3"/>
  </svg>

  <div class="logo"><span class="logo-dot"></span>Voyage Harbor</div>

  <div class="divider"></div>
  <address class="address" style="font-style:normal">
    <span class="label">Address:</span><br>
    4B Wattle Lane<br>
    Penhurst Sydney NSW 2241
  </address>

  <h1 class="consultant">Consultant Name</h1>
  <div class="contacts">
    <span class="label">Phone:</span>02 9471 3652<br>
    <span class="label">Fax:</span>02 9563 4417<br>
    sales@voyageharbor-example.com.au
  </div>
</section>

</body>
</html>
```